Ridgeway Hearth Partners Business Card

Looking for a new business card layout. We are a real estate firm w/ a logo, old design attached. Must keep the same elements on there, just need a fresh look and possible some foil accents. Looking for a simpler design w/ more modern style.

Target Market(s)

Real Estate clients

Industry/Entity Type

Real Estate Agent

Contact Information for Business Card

Font styles to use
Sans Serif

Requirements
Must have
• all elements on current biz card
Nice to have
• modern look, simpler than we have!
Should not have
• no serif fonts

```html
<!DOCTYPE html>
<html lang="en">
<head>
<meta charset="utf-8">
<title>Ridgeway Hearth Partners – Business Card</title>
<link rel="stylesheet" href="https://fonts.googleapis.com/css2?family=Montserrat:wght@500;600;800&display=swap">
<style>
  :root {
    --backdrop: #e0e1e0;
    --ink-black: #000000;
    --paper: #ffffff;
    --cyan: #1ec8e6;
    --azure: #1a9fe0;
    --text-light: #ffffff;
  }
  * { box-sizing: border-box; margin: 0; padding: 0; }
  html, body {
    width: 1200px; height: 1200px; overflow: hidden;
    background: var(--backdrop);
    font-family: "Montserrat", sans-serif;
  }
  .card {
    position: absolute; left: 198px; width: 805px; height: 461px;
  }
  .card-front { top: 102px; display: flex; background: var(--ink-black); }
  .portrait {
    width: 358px; height: 100%;
    background: linear-gradient(180deg, #ece8e1 0%, #dcc79f 35%, #d8b48e 55%, #3cc2c4 80%, #34bcc0 100%);
  }
  .front-info { position: relative; flex: 1; }
  .firm-mark {
    position: absolute; top: 138px; right: 38px;
    font-weight: 600; font-size: 14px; line-height: 18px; letter-spacing: 1.5px;
    color: var(--azure); text-transform: uppercase; white-space: nowrap;
    display: flex; align-items: center; gap: 8px;
  }
  .firm-mark .dot { width: 10px; height: 10px; background: var(--azure); }
  .agent-name {
    position: absolute; left: 54px; top: 184px;
    font-weight: 800; font-size: 29px; line-height: 36px; color: var(--cyan); letter-spacing: 0.2px;
    white-space: nowrap;
  }
  .agent-title {
    position: absolute; left: 54px; top: 226px;
    font-weight: 600; font-size: 14px; color: var(--text-light);
  }
  .contact-list { position: absolute; left: 54px; top: 256px; list-style: none; }
  .contact-list li {
    display: flex; align-items: center; height: 33.2px; white-space: nowrap;
    font-weight: 500; font-size: 13px; letter-spacing: 2px; color: var(--text-light);
  }
  .contact-list svg { width: 20px; height: 20px; margin-right: 9px; flex: none; }

  .card-back {
    top: 627px; background: var(--paper);
    border-right: 4px solid var(--cyan); border-bottom: 4px solid var(--cyan);
  }
  .back-firm {
    position: absolute; left: 0; right: 0; top: 205px;
    display: flex; justify-content: center; align-items: center; gap: 12px;
    font-weight: 600; font-size: 26px; letter-spacing: 2px;
    color: var(--azure); text-transform: uppercase;
  }
  .back-firm .dot { width: 18px; height: 18px; background: var(--azure); }
  .back-web {
    position: absolute; left: 0; right: 0; top: 430px; text-align: center;
    font-weight: 500; font-size: 13px; letter-spacing: 4.5px; color: var(--azure);
  }
</style>
</head>
<body>
  <section class="card card-front">
    <div class="portrait" role="img" aria-label="Portrait photograph of the agent"></div>
    <div class="front-info">
      <div class="firm-mark"><span class="dot"></span>Ridgeway Hearth Partners</div>
      <h1 class="agent-name">Maren Dahl</h1>
      <p class="agent-title">Principal Broker</p>
      <ul class="contact-list">
        <li>
          <svg viewBox="0 0 20 20"><circle cx="10" cy="10" r="10" fill="#1ec8e6"/><path d="M6 7.5c0 3.5 3 6.5 6.5 6.5l1.2-1.8-2-1.2-1 .8c-1-.5-1.8-1.3-2.3-2.3l.8-1-1.2-2z" fill="#000"/></svg>
          555.201.3384
        </li>
        <li>
          <svg viewBox="0 0 20 20"><circle cx="10" cy="10" r="10" fill="#1ec8e6"/><rect x="7" y="4.5" width="6" height="11" rx="1" fill="#000"/><rect x="8" y="6" width="4" height="7" fill="#1ec8e6"/></svg>
          555.201.4790
        </li>
        <li>
          <svg viewBox="0 0 20 20"><circle cx="10" cy="10" r="10" fill="#1ec8e6"/><rect x="5" y="6.5" width="10" height="7" fill="none" stroke="#000" stroke-width="1.2"/><path d="M5 6.5l5 4 5-4M5 13.5l3.5-3.5M15 13.5L11.5 10" fill="none" stroke="#000" stroke-width="1"/></svg>
          maren@ridgewayhearth.com
        </li>
        <li>
          <svg viewBox="0 0 20 20"><circle cx="10" cy="10" r="10" fill="#1ec8e6"/><circle cx="10" cy="10" r="5" fill="none" stroke="#000" stroke-width="1.3"/><path d="M5 10h10M10 5c-2 3-2 7 0 10M10 5c2 3 2 7 0 10" fill="none" stroke="#000" stroke-width="1"/></svg>
          www.RidgewayHearth.com
        </li>
        <li>
          <svg viewBox="0 0 20 20"><circle cx="10" cy="10" r="10" fill="#1ec8e6"/><path d="M10 4.5a3.5 3.5 0 0 1 3.5 3.5c0 2.6-3.5 7-3.5 7s-3.5-4.4-3.5-7A3.5 3.5 0 0 1 10 4.5z" fill="#000"/><circle cx="10" cy="8" r="1.3" fill="#1ec8e6"/></svg>
          418 NW Cedar Ln Pinebrook,OR 97000
        </li>
      </ul>
    </div>
  </section>

  <section class="card card-back">
    <div class="back-firm"><span class="dot"></span>Ridgeway Hearth Partners</div>
    <p class="back-web">www.RidgewayHearth.com</p>
  </section>
</body>
</html>
```